Attorney Business Card

I need a business card that looks professional yet modern. I am an Attorney. , I need a professional yet modern business card for my law practice. My logo and information have been uploaded. , I need a business card that looks professional yet modern. I am an Attorney. , I need a professional yet modern business card for my law practice. My logo and information have been uploaded.

Industry/Entity Type

Business

Requirements
Must have
• My logo which has been uploaded , my logo , My logo which has been uploaded , my logo

```html
<!DOCTYPE html>
<html lang="en">
<head>
<meta charset="utf-8">
<title>Ardestani Law Firm — Business Card</title>
<link rel="stylesheet" href="https://fonts.googleapis.com/css2?family=EB+Garamond:ital,wght@0,400;0,500;1,400&display=swap">
<style>
  :root {
    --page: #ffffff;
    --card: #fbfbf9;
    --rule: #5a5a5a;
    --ink: #4a4a4a;
    --accent: #3fd0f4;
  }
  * { margin: 0; padding: 0; box-sizing: border-box; }
  html, body { width: 1200px; height: 1000px; overflow: hidden; background: var(--page); }
  body { position: relative; font-family: "EB Garamond", Georgia, serif; color: var(--ink); }

  .card {
    position: absolute;
    width: 687px; height: 393px;
    background: var(--card);
    border: 1px solid var(--rule);
  }
  .card--front { left: 257px; top: 88px; }
  .card--back  { left: 256px; top: 516px; }

  .panel {
    position: absolute;
    border: 1px solid var(--rule);
  }
  .card--front .panel { left: 45px; top: 88px; width: 594px; height: 214px; }
  .card--back .panel  { left: 44px; top: 46px; width: 595px; height: 289px; }

  .row {
    position: absolute; left: 0; right: 0;
    display: flex; align-items: center; justify-content: center;
  }
  .row + .row { border-top: 1px solid var(--rule); }

  .caps {
    text-transform: uppercase;
    letter-spacing: 2.4px;
    font-size: 19px;
    font-weight: 500;
    line-height: 1;
  }
  .num { letter-spacing: 1.2px; font-weight: 400; }

  .divider {
    display: inline-block; width: 1px; height: 19px;
    background: var(--accent);
  }

  /* front */
  .identity { top: 0; height: 141px; }
  .brand-mark {
    position: absolute; left: 36px; top: 28px;
    width: 94px; height: 86px;
    display: flex; flex-direction: column; align-items: center; justify-content: center; gap: 6px;
  }
  .brand-mark__dot {
    width: 44px; height: 44px; border-radius: 50%;
    border: 2px solid var(--accent);
  }
  .brand-mark__name {
    color: var(--accent);
    font-size: 11px; font-weight: 500;
    letter-spacing: 1.2px; text-transform: uppercase;
  }
  .holder {
    position: absolute; left: 150px; right: 40px; top: 44px;
    text-align: center;
  }
  .holder__name { display: block; }
  .holder__title {
    display: block; margin-top: 10px;
    font-style: italic; font-size: 24px; font-weight: 400;
  }
  .online { top: 141px; height: 72px; gap: 36px; }

  /* back */
  .address { top: 0; height: 149px; flex-direction: column; gap: 17px; }
  .phones  { top: 149px; height: 68px; gap: 36px; }
  .mobile  { top: 217px; height: 71px; }
</style>
</head>
<body>

  <section class="card card--front">
    <div class="panel">
      <div class="row identity">
        <div class="brand-mark">
          <span class="brand-mark__dot"></span>
          <span class="brand-mark__name">Ardestani</span>
        </div>
        <div class="holder">
          <span class="holder__name caps">Daniel Ardestani, Esquire</span>
          <span class="holder__title">Attorney At Law</span>
        </div>
      </div>
      <div class="row online">
        <span class="caps">daniel@adfirm.com</span>
        <span class="divider"></span>
        <span class="caps">adfirm.com</span>
      </div>
    </div>
  </section>

  <section class="card card--back">
    <div class="panel">
      <div class="row address">
        <span class="caps"><span class="num">8120</span> Crestview Boulevard</span>
        <span class="caps">Penthouse</span>
        <span class="caps">Westbrook, California <span class="num">90418</span></span>
      </div>
      <div class="row phones">
        <span class="caps"><span class="num">555.210.4400</span> Tel</span>
        <span class="divider"></span>
        <span class="caps"><span class="num">555.210.4401</span> Fax</span>
      </div>
      <div class="row mobile">
        <span class="caps"><span class="num">555.318.7720</span> Mobile</span>
      </div>
    </div>
  </section>

</body>
</html>
```